Diversity report of banking market in Europe

*Power point presentation style - rather than corporate brochure*
We are an executive recruitment firm who will be sending a report to all our senior clients. We need a designer to make it look eye catching, slick and professional for our audience. The document will be read mainly by PDF so the type of font and size will be very important as will the size of each page.

We have all the content but may need guidance on the amount of text, the size of graphs and inserting some pictures/vectors etc. We can provide more text or cut text back it it helps the design. We can find more graphs if this helps to fill a page

Industry/Entity Type

Investment Banking

Font styles to use
Sans Serif

Colors
0255a3
33b8a4
85cae6
cfeae6
ffffff

Requirements
Must have
• Colours:
11, 29, 49
70, 165, 175
Nice to have
• Have added two example Marvenholt documents that we feel are clean and professional. Please use these are our attempt as a guide line to how was want the document to look and feel and flow. Happy to add additional pictures or design to fill out pages. Cant steal actual pictures from marvenholt report

```html
<!DOCTYPE html>
<html lang="en">
<head>
<meta charset="utf-8">
<title>Diversity Review in Corporate Credit – Halloway Crest</title>
<link rel="stylesheet" href="https://fonts.googleapis.com/css2?family=Montserrat:wght@300;400;500;600;700&display=swap">
<style>
:root{
  --backdrop:#7d8184;
  --navy:#0b1d31;
  --navy-mid:#1b2f63;
  --teal:#46a5af;
  --teal-bright:#3a9ca0;
  --bar-navy:#1f3566;
  --bar-teal:#49aab2;
  --blue:#1b72b8;
  --sky:#85cae6;
  --green:#10834f;
  --green-dark:#0c5a55;
  --mint:#cfeae6;
  --ink:#1d2a3c;
  --white:#ffffff;
}
*{margin:0;padding:0;box-sizing:border-box}
html,body{width:1200px;height:880px;overflow:hidden;background:var(--backdrop)}
body{position:relative;font-family:"Montserrat",Arial,sans-serif;color:var(--ink)}
.page{position:absolute;width:543px;height:383px;overflow:hidden;background:var(--white)}
.page--cover{left:46px;top:43px;background:linear-gradient(160deg,#0f2447 0%,#1b3170 55%,#243c8a 100%)}
.page--p4{left:610px;top:43px}
.page--p5{left:46px;top:452px}
.page--p3{left:610px;top:452px}

/* cover */
.cover-brand{position:absolute;left:26px;top:24px;font-size:11.5px;font-weight:500;letter-spacing:.5px;color:var(--white);text-transform:uppercase}
.cover-art{position:absolute;left:330px;top:30px;width:213px;height:353px;background:radial-gradient(ellipse at 60% 45%,rgba(70,165,175,.45),rgba(36,60,138,0) 70%)}
.cover-title{position:absolute;left:24px;top:158px;font-size:44.5px;line-height:40.5px;font-weight:400;color:var(--teal);letter-spacing:.5px}
.cover-sub{position:absolute;left:26px;top:331px;font-size:6.6px;letter-spacing:2.6px;line-height:8px;color:var(--white)}
.cover-author{position:absolute;left:26px;top:354px;font-size:4.8px;letter-spacing:1.8px;color:var(--white)}

/* content page furniture */
.page-header{position:absolute;left:0;top:0;width:100%;height:30px;background:linear-gradient(90deg,var(--teal) 0%,var(--teal) 28%,#1a3a55 52%,var(--navy) 70%)}
.page-header .brand{position:absolute;right:26px;top:12px;font-size:9.5px;font-weight:500;letter-spacing:.4px;color:var(--white);text-transform:uppercase}
.page-footer{position:absolute;left:0;bottom:0;width:100%;height:5px;background:var(--teal)}
.page-num{position:absolute;right:5px;bottom:10px;font-size:5px;color:var(--teal)}
.divider{position:absolute;left:187px;top:52px;width:.6px;height:312px;background:#b7d9dc}

.intro{position:absolute;left:26px;top:48px;width:157px}
.intro h1{font-size:12.5px;font-weight:300;color:var(--teal);margin-bottom:6px}
.intro h2{font-size:6.2px;font-weight:600;color:var(--navy);margin-bottom:5px}
.intro p{font-size:4.1px;line-height:5.4px;color:#333;margin-bottom:5px}

.section-title{position:absolute;left:193px;top:51px;font-size:6.3px;font-weight:600;color:var(--teal-bright);letter-spacing:.2px}

.bars{position:absolute;left:193px;top:74px;width:330px}
.bar-row{position:absolute;left:0;height:12px;width:330px}
.bar-row .label{position:absolute;left:0;top:0;width:45px;font-size:4.4px;line-height:4.8px;color:var(--ink)}
.bars--flat .label{text-align:right;width:44px}
.bar{position:absolute;left:49px;top:0;height:11px;display:flex}
.bar span{display:block;height:100%;font-size:4.6px;color:var(--white);padding-left:5px;line-height:11px}
.bar .m{background:var(--bar-navy)}
.bar .f{background:var(--bar-teal)}
.bars--depth .bar{border-top:2px solid var(--navy);box-shadow:2px -1px 0 #27385e}
.bars--depth .bar span{line-height:9px}
.legend{position:absolute;left:49px;top:82px;font-size:4.4px;color:var(--ink);display:flex;gap:12px}
.legend i{display:inline-block;width:4px;height:4px;margin-right:3px;vertical-align:-.5px}
.legend .lm{background:var(--bar-navy)}
.legend .lf{background:var(--bar-teal)}

.summary{position:absolute;left:193px;top:172px;width:326px;font-size:4.1px;line-height:5.3px;color:#333}

.charts{position:absolute;left:193px;top:200px;width:330px;height:140px}
.charts svg{position:absolute;left:0;top:0}
.stat{position:absolute;font-weight:600;color:var(--navy);text-align:center;line-height:8px}
.stat small{display:block;font-size:4.2px;font-weight:500;line-height:5px;letter-spacing:.2px}
.stat b{display:block;font-size:8.6px;font-weight:600}
.figure{position:absolute;width:8px;height:34px;border-radius:3px;background:linear-gradient(180deg,#57b8b9,#2e7f8c)}
.figure--dark{background:linear-gradient(180deg,#4a63c7,#27368a)}

.caption{position:absolute;top:342px;width:158px;font-size:4.1px;line-height:5.2px;color:#333}
.caption--a{left:193px}
.caption--b{left:360px}
</style>
</head>
<body>

<!-- Cover -->
<section class="page page--cover">
  <div class="cover-brand">Halloway Crest</div>
  <div class="cover-art" role="img" aria-label="Illustration of a woman and a man standing on two tall plinths of different heights"></div>
  <h1 class="cover-title">DIVERSITY<br>REVIEW IN<br>CORPORATE<br>CREDIT</h1>
  <p class="cover-sub">Gender &amp; Ethnicity within Credit Investment<br>Management &amp; Leveraged Finance</p>
  <p class="cover-author">Written by Nadia Corwen</p>
</section>

<!-- Page 4 : 3D pies -->
<section class="page page--p4">
  <header class="page-header"><span class="brand">Halloway Crest</span></header>
  <div class="intro">
    <h1>Introduction</h1>
    <h2>Halloway Crest, A Diversity Review</h2>
    <p>Gender is profoundly the over-riding ‘diversity’ issue within asset management, however, the escalating Black Lives Matter movement and global protests over systemic racism is also catalysing demand for corporations to take action and make change to close both the gender and ethnicity gap within their organisation’s. There are many public articles written by leading media outlets creating targeted campaigns to shame industries with unbalanced representation. We see diversity reviews by news outlets such as the Northgate Review more prominently focused on senior staff levels, these articles looking to “shine a light” on the lack of female diversity at board level and within Private Equity investment teams themselves. Where the numbers are less transparent, I’m referring to the opaque levels of representation of female and ethnic minorities at the mid-level and junior levels of staff, a war is being waged by Investment managers and banks to address the lack of diversity within their teams. It has become a common theme and a common request to any highly established search firm in the Credit markets, to help address diversity. In this report we look to analyse the figures, in some places we may draw conclusions to the data, and in others allow you to interpret the figures via your own methods. What we will achieve by this report, is to give you, the Heads of business and senior HR professionals, the statistics you need to understand what the market actually looks like, the levels of female professionals in the market as a whole, and then broken down by strategy and seniority. The number of females &amp; ethnic minorities working not only in your market, but adjacent markets and importantly the market that feeds all of these buyside strategies, the Investment Banking teams. Beyond this we have analysed the market that feeds the Financial Services industry as a whole, the diversity across university placements. Lastly we have attempted to analyse and compare the diversity of the Investment Banking and Investment Management industry in comparison to other mathematically based industries.</p>
    <p>Halloway Crest is a Search firm with an established and credible management team. We pride ourselves on the depth and accuracy of our research. Our investment in research is a very clear differentiating factor which has aided in our long and successful track-record in Credit, but also given us the opportunity to produce this report. We are able to break these numbers down line by line, to show how we calculated these numbers via our research. We are also happy to present the hard-data compiled for this report in a data-set format.</p>
    <p>Halloway Crest is uniquely positioned to produce this report. Our exhaustive approach to tracking information enables us to conduct a gender and ethnicity review and identify current trends. We have reviewed 420 teams within 358 firms across Direct Lending, CLOs, Distressed Debt &amp; Specials Sits. Alongside this effort we have analysed diversity in leveraged finance, restructuring and distressed debt in Investment Banking &amp; Advisory Firms</p>
  </div>
  <div class="divider"></div>
  <h2 class="section-title">GENDER DIVERSITY ACROSS EACH STRATEGY</h2>
  <div class="bars bars--depth">
    <div class="bar-row" style="top:0"><span class="label">BANKS &amp;<br>ADVISORY</span><div class="bar"><span class="m" style="width:215px">1574</span><span class="f" style="width:46px">340</span></div></div>
    <div class="bar-row" style="top:20px"><span class="label" style="top:3px">DISTRESSED</span><div class="bar"><span class="m" style="width:155px">1132</span><span class="f" style="width:14px">91</span></div></div>
    <div class="bar-row" style="top:40px"><span class="label" style="top:3px">CLO’S</span><div class="bar"><span class="m" style="width:106px">776</span><span class="f" style="width:20px">134</span></div></div>
    <div class="bar-row" style="top:61px"><span class="label">DIRECT<br>LENDING</span><div class="bar"><span class="m" style="width:195px">1427</span><span class="f" style="width:33px">240</span></div></div>
    <div class="legend"><span><i class="lm"></i>MALE</span><span><i class="lf"></i>FEMALE</span></div>
  </div>
  <p class="summary">The overall gender diversity levels across each strategy will be explored further in this report. The below chart is a clear visualisation of male to female ratio’s for Investment Professionals working in Direct Lending, Single Name Distressed, CLOs and Leveraged Finance. Direct Lending as an asset class has the closest male to female diversity ratio as found in banking. We are tracking a 17% gender diversity in Banking and a 14% gender diversity in Direct Lending.</p>
  <div class="charts">
    <svg width="330" height="140" viewBox="0 0 330 140" aria-label="Pie charts of gender and ethnicity split">
      <defs>
        <linearGradient id="base4" x1="0" x2="1"><stop offset="0" stop-color="#8b8f93"/><stop offset=".45" stop-color="#f4f4f4"/><stop offset="1" stop-color="#8b8f93"/></linearGradient>
        <linearGradient id="blueTop4" x1="0" y1="0" x2="1" y2="1"><stop offset="0" stop-color="#2a8ad0"/><stop offset="1" stop-color="#125c9c"/></linearGradient>
        <linearGradient id="greenTop4" x1="0" y1="0" x2="1" y2="1"><stop offset="0" stop-color="#139156"/><stop offset="1" stop-color="#0b6a3c"/></linearGradient>
      </defs>
      <g transform="translate(78 66)">
        <ellipse cx="0" cy="26" rx="60" ry="32" fill="#9a9ea2"/>
        <ellipse cx="0" cy="18" rx="60" ry="32" fill="url(#base4)"/>
        <ellipse cx="0" cy="10" rx="52" ry="28" fill="#0f4e86"/>
        <path d="M0 0 L45 14 A52 28 0 1 1 48.9 -9.6 Z" fill="url(#blueTop4)"/>
        <path d="M6 14 L54.9 4.4 A52 28 0 0 1 51 28 Z" fill="#2e7f86"/>
        <path d="M6 4 L54.9 -5.6 A52 28 0 0 1 51 18 Z" fill="#6fc7cf"/>
        <line x1="-20" y1="-6" x2="-20" y2="-58" stroke="#6fc7cf" stroke-width=".5"/>
        <line x1="40" y1="6" x2="40" y2="-58" stroke="#6fc7cf" stroke-width=".5"/>
      </g>
      <g transform="translate(246 66)">
        <ellipse cx="0" cy="26" rx="60" ry="32" fill="#9a9ea2"/>
        <ellipse cx="0" cy="18" rx="60" ry="32" fill="url(#base4)"/>
        <ellipse cx="0" cy="10" rx="52" ry="28" fill="#0a5a33"/>
        <path d="M0 0 L45 14 A52 28 0 1 1 48.9 -9.6 Z" fill="url(#greenTop4)"/>
        <path d="M6 14 L54.9 4.4 A52 28 0 0 1 51 28 Z" fill="#5d6b78"/>
        <path d="M6 4 L54.9 -5.6 A52 28 0 0 1 51 18 Z" fill="#c9d9ec"/>
        <line x1="-20" y1="-6" x2="-20" y2="-58" stroke="#6fc7cf" stroke-width=".5"/>
        <line x1="40" y1="6" x2="40" y2="-58" stroke="#6fc7cf" stroke-width=".5"/>
      </g>
    </svg>
    <div class="stat" style="left:40px;top:4px"><small>MALE</small><b>4909</b><b>86%</b></div>
    <div class="stat" style="left:104px;top:4px"><small>FEMALE</small><b>805</b><b>14%</b></div>
    <div class="stat" style="left:212px;top:4px"><small>WHITE</small><b>5042</b></div>
    <div class="stat" style="left:272px;top:4px;text-align:left"><small>ETHNIC<br>MINORITIES</small><b>672</b></div>
  </div>
  <p class="caption caption--a">There are currently 5714 professionals working across Direct Lending, Single Name Distressed, CLOs and Leveraged Finance in Europe. 805 (14%) are female and 4909 (86%) are male</p>
  <p class="caption caption--b">672 investment professionals working in across Direct Lending, Single Name Distressed, CLOs and Leveraged Finance in Europe fall within Ethnic Minorities whereas 5042 of the work force is White</p>
  <span class="page-num">4</span>
  <div class="page-footer"></div>
</section>

<!-- Page 5 : donuts -->
<section class="page page--p5">
  <header class="page-header"><span class="brand">Halloway Crest</span></header>
  <div class="intro">
    <h1>Introduction</h1>
    <h2>Halloway Crest, A Diversity Review</h2>
    <p>Gender is profoundly the over-riding ‘diversity’ issue within asset management, however, the escalating Black Lives Matter movement and global protests over systemic racism is also catalysing demand for corporations to take action and make change to close both the gender and ethnicity gap within their organisation’s. There are many public articles written by leading media outlets creating targeted campaigns to shame industries with unbalanced representation. We see diversity reviews by news outlets such as the Northgate Review more prominently focused on senior staff levels, these articles looking to “shine a light” on the lack of female diversity at board level and within Private Equity investment teams themselves. Where the numbers are less transparent, I’m referring to the opaque levels of representation of female and ethnic minorities at the mid-level and junior levels of staff, a war is being waged by Investment managers and banks to address the lack of diversity within their teams. It has become a common theme and a common request to any highly established search firm in the Credit markets, to help address diversity. In this report we look to analyse the figures, in some places we may draw conclusions to the data, and in others allow you to interpret the figures via your own methods. What we will achieve by this report, is to give you, the Heads of business and senior HR professionals, the statistics you need to understand what the market actually looks like, the levels of female professionals in the market as a whole, and then broken down by strategy and seniority. The number of females &amp; ethnic minorities working not only in your market, but adjacent markets and importantly the market that feeds all of these buyside strategies, the Investment Banking teams. Beyond this we have analysed the market that feeds the Financial Services industry as a whole, the diversity across university placements. Lastly we have attempted to analyse and compare the diversity of the Investment Banking and Investment Management industry in comparison to other mathematically based industries.</p>
    <p>Halloway Crest is a Search firm with an established and credible management team. We pride ourselves on the depth and accuracy of our research. Our investment in research is a very clear differentiating factor which has aided in our long and successful track-record in Credit, but also given us the opportunity to produce this report. We are able to break these numbers down line by line, to show how we calculated these numbers via our research. We are also happy to present the hard-data compiled for this report in a data-set format.</p>
    <p>Halloway Crest is uniquely positioned to produce this report. Our exhaustive approach to tracking information enables us to conduct a gender and ethnicity review and identify current trends. We have reviewed 420 teams within 358 firms across Direct Lending, CLOs, Distressed Debt &amp; Specials Sits. Alongside this effort we have analysed diversity in leveraged finance, restructuring and distressed debt in Investment Banking &amp; Advisory Firms</p>
  </div>
  <div class="divider"></div>
  <h2 class="section-title">GENDER DIVERSITY ACROSS EACH STRATEGY</h2>
  <div class="bars bars--flat">
    <div class="bar-row" style="top:0"><span class="label">BANKS &amp;<br>ADVISORY</span><div class="bar"><span class="m" style="width:215px">1574</span><span class="f" style="width:47px">340</span></div></div>
    <div class="bar-row" style="top:20px"><span class="label" style="top:3px">DISTRESSED</span><div class="bar"><span class="m" style="width:155px">1132</span><span class="f" style="width:13px">91</span></div></div>
    <div class="bar-row" style="top:40px"><span class="label" style="top:3px">CLO’S</span><div class="bar"><span class="m" style="width:106px">776</span><span class="f" style="width:19px">134</span></div></div>
    <div class="bar-row" style="top:61px"><span class="label">DIRECT<br>LENDING</span><div class="bar"><span class="m" style="width:195px">1427</span><span class="f" style="width:33px">240</span></div></div>
    <div class="legend"><span><i class="lm"></i>MALE</span><span><i class="lf"></i>FEMALE</span></div>
  </div>
  <p class="summary">The overall gender diversity levels across each strategy will be explored further in this report. The below chart is a clear visualisation of male to female ratio’s for Investment Professionals working in Direct Lending, Single Name Distressed, CLOs and Leveraged Finance. Direct Lending as an asset class has the closest male to female diversity ratio as found in banking. We are tracking a 17% gender diversity in Banking and a 14% gender diversity in Direct Lending.</p>
  <div class="charts">
    <svg width="330" height="140" viewBox="0 0 330 140" aria-label="Donut charts of gender and ethnicity split">
      <defs>
        <linearGradient id="blueRing" x1="0" y1="0" x2="1" y2="1"><stop offset="0" stop-color="#1b80c4"/><stop offset="1" stop-color="#1f3566"/></linearGradient>
        <linearGradient id="greenRing" x1="0" y1="0" x2="1" y2="1"><stop offset="0" stop-color="#139156"/><stop offset="1" stop-color="#0c4f52"/></linearGradient>
      </defs>
      <g transform="translate(85 66)">
        <circle r="46" fill="none" stroke="url(#blueRing)" stroke-width="14"/>
        <circle r="46" fill="none" stroke="#8fd3df" stroke-width="14" stroke-dasharray="40.5 289" transform="rotate(28)"/>
      </g>
      <g transform="translate(232 66)">
        <circle r="46" fill="none" stroke="url(#greenRing)" stroke-width="14"/>
        <circle r="46" fill="none" stroke="#8fd3df" stroke-width="14" stroke-dasharray="34 289" transform="rotate(55)"/>
      </g>
    </svg>
    <div class="stat" style="left:26px;top:8px"><small>MALE</small><b>4909</b><b>86%</b></div>
    <div class="stat" style="left:124px;top:104px"><small>FEMALE</small><b>805</b><b>14%</b></div>
    <div class="stat" style="left:186px;top:8px"><small>WHITE</small><b>5042</b></div>
    <div class="stat" style="left:268px;top:104px;text-align:left"><small>ETHNIC<br>MINORITIES</small><b>672</b></div>
  </div>
  <p class="caption caption--a">There are currently 5714 professionals working across Direct Lending, Single Name Distressed, CLOs and Leveraged Finance in Europe. 805 (14%) are female and 4909 (86%) are male</p>
  <p class="caption caption--b">672 investment professionals working in across Direct Lending, Single Name Distressed, CLOs and Leveraged Finance in Europe fall within Ethnic Minorities whereas 5042 of the work force is White</p>
  <span class="page-num">5</span>
  <div class="page-footer"></div>
</section>

<!-- Page 3 : 3D pies with figures -->
<section class="page page--p3">
  <header class="page-header"><span class="brand">Halloway Crest</span></header>
  <div class="intro">
    <h1>Introduction</h1>
    <h2>Halloway Crest, A Diversity Review</h2>
    <p>Gender is profoundly the over-riding ‘diversity’ issue within asset management, however, the escalating Black Lives Matter movement and global protests over systemic racism is also catalysing demand for corporations to take action and make change to close both the gender and ethnicity gap within their organisation’s. There are many public articles written by leading media outlets creating targeted campaigns to shame industries with unbalanced representation. We see diversity reviews by news outlets such as the Northgate Review more prominently focused on senior staff levels, these articles looking to “shine a light” on the lack of female diversity at board level and within Private Equity investment teams themselves. Where the numbers are less transparent, I’m referring to the opaque levels of representation of female and ethnic minorities at the mid-level and junior levels of staff, a war is being waged by Investment managers and banks to address the lack of diversity within their teams. It has become a common theme and a common request to any highly established search firm in the Credit markets, to help address diversity. In this report we look to analyse the figures, in some places we may draw conclusions to the data, and in others allow you to interpret the figures via your own methods. What we will achieve by this report, is to give you, the Heads of business and senior HR professionals, the statistics you need to understand what the market actually looks like, the levels of female professionals in the market as a whole, and then broken down by strategy and seniority. The number of females &amp; ethnic minorities working not only in your market, but adjacent markets and importantly the market that feeds all of these buyside strategies, the Investment Banking teams. Beyond this we have analysed the market that feeds the Financial Services industry as a whole, the diversity across university placements. Lastly we have attempted to analyse and compare the diversity of the Investment Banking and Investment Management industry in comparison to other mathematically based industries.</p>
    <p>Halloway Crest is a Search firm with an established and credible management team. We pride ourselves on the depth and accuracy of our research. Our investment in research is a very clear differentiating factor which has aided in our long and successful track-record in Credit, but also given us the opportunity to produce this report. We are able to break these numbers down line by line, to show how we calculated these numbers via our research. We are also happy to present the hard-data compiled for this report in a data-set format.</p>
    <p>Halloway Crest is uniquely positioned to produce this report. Our exhaustive approach to tracking information enables us to conduct a gender and ethnicity review and identify current trends. We have reviewed 420 teams within 358 firms across Direct Lending, CLOs, Distressed Debt &amp; Specials Sits. Alongside this effort we have analysed diversity in leveraged finance, restructuring and distressed debt in Investment Banking &amp; Advisory Firms</p>
  </div>
  <div class="divider"></div>
  <h2 class="section-title">GENDER DIVERSITY ACROSS EACH STRATEGY</h2>
  <div class="bars bars--depth">
    <div class="bar-row" style="top:0"><span class="label">BANKS &amp;<br>ADVISORY</span><div class="bar"><span class="m" style="width:215px">1574</span><span class="f" style="width:46px">340</span></div></div>
    <div class="bar-row" style="top:20px"><span class="label" style="top:3px">DISTRESSED</span><div class="bar"><span class="m" style="width:155px">1132</span><span class="f" style="width:14px">91</span></div></div>
    <div class="bar-row" style="top:40px"><span class="label" style="top:3px">CLO’S</span><div class="bar"><span class="m" style="width:106px">776</span><span class="f" style="width:20px">134</span></div></div>
    <div class="bar-row" style="top:61px"><span class="label">DIRECT<br>LENDING</span><div class="bar"><span class="m" style="width:195px">1427</span><span class="f" style="width:33px">240</span></div></div>
    <div class="legend"><span><i class="lm"></i>MALE</span><span><i class="lf"></i>FEMALE</span></div>
  </div>
  <p class="summary">The overall gender diversity levels across each strategy will be explored further in this report. The below chart is a clear visualisation of male to female ratio’s for Investment Professionals working in Direct Lending, Single Name Distressed, CLOs and Leveraged Finance. Direct Lending as an asset class has the closest male to female diversity ratio as found in banking. We are tracking a 17% gender diversity in Banking and a 14% gender diversity in Direct Lending.</p>
  <div class="charts">
    <svg width="330" height="140" viewBox="0 0 330 140" aria-label="Pie charts of gender and ethnicity split">
      <defs>
        <linearGradient id="base3" x1="0" x2="1"><stop offset="0" stop-color="#8b8f93"/><stop offset=".45" stop-color="#f4f4f4"/><stop offset="1" stop-color="#8b8f93"/></linearGradient>
        <linearGradient id="blueTop3" x1="0" y1="0" x2="1" y2="1"><stop offset="0" stop-color="#2a8ad0"/><stop offset="1" stop-color="#125c9c"/></linearGradient>
        <linearGradient id="greenTop3" x1="0" y1="0" x2="1" y2="1"><stop offset="0" stop-color="#139156"/><stop offset="1" stop-color="#0b6a3c"/></linearGradient>
      </defs>
      <g transform="translate(78 70)">
        <ellipse cx="0" cy="26" rx="60" ry="32" fill="#9a9ea2"/>
        <ellipse cx="0" cy="18" rx="60" ry="32" fill="url(#base3)"/>
        <ellipse cx="0" cy="10" rx="52" ry="28" fill="#0f4e86"/>
        <path d="M0 0 L45 14 A52 28 0 1 1 48.9 -9.6 Z" fill="url(#blueTop3)"/>
        <path d="M6 14 L54.9 4.4 A52 28 0 0 1 51 28 Z" fill="#2e7f86"/>
        <path d="M6 4 L54.9 -5.6 A52 28 0 0 1 51 18 Z" fill="#6fc7cf"/>
        <line x1="-40" y1="0" x2="-40" y2="-48" stroke="#6fc7cf" stroke-width=".5"/>
        <line x1="40" y1="6" x2="40" y2="-48" stroke="#6fc7cf" stroke-width=".5"/>
      </g>
      <g transform="translate(246 70)">
        <ellipse cx="0" cy="26" rx="60" ry="32" fill="#9a9ea2"/>
        <ellipse cx="0" cy="18" rx="60" ry="32" fill="url(#base3)"/>
        <ellipse cx="0" cy="10" rx="52" ry="28" fill="#0a5a33"/>
        <path d="M0 0 L45 14 A52 28 0 1 1 48.9 -9.6 Z" fill="url(#greenTop3)"/>
        <path d="M6 14 L54.9 4.4 A52 28 0 0 1 51 28 Z" fill="#5d6b78"/>
        <path d="M6 4 L54.9 -5.6 A52 28 0 0 1 51 18 Z" fill="#c9d9ec"/>
        <line x1="-40" y1="0" x2="-40" y2="-48" stroke="#6fc7cf" stroke-width=".5"/>
        <line x1="30" y1="6" x2="30" y2="-48" stroke="#6fc7cf" stroke-width=".5"/>
      </g>
    </svg>
    <div class="figure" role="img" aria-label="Small figure of a man standing on the male share" style="left:63px;top:14px"></div>
    <div class="figure figure--dark" role="img" aria-label="Small figure of a woman standing on the female share" style="left:103px;top:36px"></div>
    <div class="figure" role="img" aria-label="Small figure of a man standing on the white share" style="left:231px;top:14px"></div>
    <div class="figure figure--dark" role="img" aria-label="Small figure of a woman standing on the ethnic minorities share" style="left:267px;top:36px"></div>
    <div class="stat" style="left:22px;top:8px"><small>MALE</small><b>4909</b><b>86%</b></div>
    <div class="stat" style="left:102px;top:8px"><small>FEMALE</small><b>805</b><b>14%</b></div>
    <div class="stat" style="left:192px;top:8px"><small>WHITE</small><b>5042</b></div>
    <div class="stat" style="left:264px;top:8px;text-align:left"><small>ETHNIC<br>MINORITIES</small><b>672</b></div>
  </div>
  <p class="caption caption--a">There are currently 5714 professionals working across Direct Lending, Single Name Distressed, CLOs and Leveraged Finance in Europe. 805 (14%) are female and 4909 (86%) are male</p>
  <p class="caption caption--b">672 investment professionals working in across Direct Lending, Single Name Distressed, CLOs and Leveraged Finance in Europe fall within Ethnic Minorities whereas 5042 of the work force is White</p>
  <span class="page-num">3</span>
  <div class="page-footer"></div>
</section>

</body>
</html>
```